Broschüren-Design für Verkauf von Produkten aus Holz
Die Kommunikation mit dem Designer TAP war durchweg einwandfrei! Änderungswünsche wurden in kürzester Zeit umgesetzt. Jederzeit gerne wieder!
Zielgruppe
Seit über 60 Jahren fertigt die Brenzel GmbH & Co. KG Produkte aus Holz.
Zielgruppe sind Küchenstudios .
Aufgabenstellung
Brenzel-Küchenstudio Broschüre/Katalog
Aufgabenstellung:
Es soll ein Katalog (PDF zum Blättern & Druckversion) erstellt werden in 3 Sprachen speziell für Küchenstudios, aufgeteilt in 6 Rubriken (je Rubrik 2-6 Seiten) + ansprechendes Deckblatt mit unserem Logo und einem Slogan aus dem sinngemäß hervorgeht, dass es sich bei unseren Produkten um maßangefertigte Unikate aus der Natur handelt. Relativ wenig Text Gesamtumfang ca. 24-30 Seiten.
Rubriken:
- Holzarten kgz + durchgehend
- Thekenplatte & Thekenaufsätze
- Küchenarbeitsplatten
- Massivholzfronten
- Tische/Tischplatten
- Schneidbretter/Hackklotz
- Magnetmesserblöcke
Ziel:
Es soll vermittelt werden:
- Massivholz passt nahezu zu jeder Küche
- In Küchen Akzente mit Massivholzkomponenten zu setzen und diese damit aufzuwerten.
- Auf Wunschmaß individuell in Deutschland gefertigt
- Erweiterungen & Austausch auf vorhandenen Küchen möglich
Unsere Grobvorstellung:
1. Innenseite: Wir über uns... mit Bildern der Ansprechpartner sowie Luftbild Firma
2. Seite: Inhaltsverzeichnis mit Seitenzahl der erhältlichen Produkte (Rubriken)
Ab Seite 3: Bilder der einzelnen Rubriken mit KLEINEN Textfelder, diese werden nachträglich von uns bearbeitet/erstellt
Letzte Seite: Informationen über Lieferung & Lieferzeiten
Rückseite: Basierend auf Deckblatt und unserem Logo (nicht all zu groß) mit Adress & Kontaktdaten
Die Bilder für die einzelnen Rubriken werden von uns gestellt, ergänzend sollen passende Bilder aus verschiedenen Quellen zu den verschiedenen Rubriken hinzugezogen werden, die mit entsprechender Genehmigung verwendet werden dürfen.
Ansonsten steht der Gestaltung und dem Design keine weiteren Vorgaben im Weg.

```html
<!DOCTYPE html>
<html lang="de">
<head>
<meta charset="utf-8">
<title>Holzarten – Katalog</title>
<link rel="stylesheet" href="https://fonts.googleapis.com/css2?family=Work+Sans:ital,wght@0,200;0,400;0,500;0,700;1,400&display=swap">
<style>
:root{
  --backdrop:#d6d3da;
  --paper:#ffffff;
  --ink:#2b2b2b;
  --ink-soft:#555555;
  --rule:#8a8a8a;
  --wood-light:#e9c9a6;
  --wood-mid:#deb68e;
  --wood-edge:#d2a47a;
}
*{margin:0;padding:0;box-sizing:border-box}
html,body{width:1200px;height:959px;overflow:hidden;background:var(--backdrop)}
body{font-family:"Work Sans",Helvetica,Arial,sans-serif;color:var(--ink);position:relative}
.spread{position:absolute;left:96px;top:124px;width:1007px;height:712px;background:var(--paper)}
.page-title{position:absolute;left:93px;top:58px;font-weight:200;font-size:36px;letter-spacing:-.5px;line-height:1;color:var(--ink)}
.page-title--vertical{left:auto;top:auto;right:12px;top:53px;writing-mode:vertical-rl;transform:rotate(180deg);font-size:31px;letter-spacing:0}
.swatch{display:block;background:linear-gradient(90deg,var(--wood-light) 0%,var(--wood-mid) 55%,var(--wood-light) 82%,var(--wood-edge) 84%,var(--wood-edge) 100%)}
.card{position:absolute}
.card h2{font-weight:500;font-size:8px;line-height:9.3px;letter-spacing:.1px}
.card .subtitle{font-style:italic;font-size:5.8px;line-height:8.3px;color:var(--ink-soft)}
.spec{font-size:3.9px;line-height:5.9px;color:var(--ink)}
.spec b{font-weight:700}
.card--tall{width:92px}
.card--tall .swatch{width:78.5px;height:103px;margin-bottom:6px}
.card--tall .subtitle{margin-top:6px}
.card--tall .spec{margin-top:6px}
.card--wide{width:115px}
.card--wide .swatch{width:115px;height:67px;margin-bottom:4px}
.card--wide .subtitle{margin-top:3px;padding-bottom:3px;border-bottom:.6px solid var(--rule)}
.card--wide .spec-grid{display:grid;grid-template-columns:56px 1fr;margin-top:4px}
.card--wide .spec-grid .spec:last-child{border-left:.6px solid var(--ink);padding-left:6px;padding-bottom:2px}
.card--wide .spec-grid .spec:first-child{padding-right:3px}
.divider{position:absolute;width:.7px;background:var(--rule)}
</style>
</head>
<body>
<div class="spread">
  <!-- left page -->
  <h1 class="page-title">HOLZARTEN</h1>
  <div class="divider" style="left:189px;top:100px;height:562px"></div>
  <div class="divider" style="left:299px;top:100px;height:562px"></div>

  <article class="card card--tall" style="left:93.5px;top:100px">
    <span class="swatch" role="img" aria-label="Holzmuster europäischer Ahorn"></span>
    <h2>Massivholzplatte einschichtig europäischer Ahorn, Möbelbauplatte</h2>
    <p class="subtitle">(Érable européen, lamelles continues)</p>
    <p class="spec"><b>VERFÜGBARE PLATTENSTÄRKEN:</b><br>19, 26, 40, 45 mm<br><b>QUALITÄT:</b> Meisterqualität durchgehende Lamellen (blockverleimt) mit fallender Breite ca. 40 - 80 mm<br><b>SORTIERUNG:</b> A/B<br><b>OBERSEITE:</b> keine Äste, ohne Kern, einheitliche Farbe u. Struktur<br><b>UNTERSEITE:</b> keine Äste, etwas Kern, natürliche Farbdifferenzen erlaubt<br><b>BOT. BEZ.:</b> Acer pseudoplatanus L. wasserfest formaldehydfrei verleimt (D3 nach DIN/EN 204) nur für den Innenbereich<br><b>HOLZFEUCHTE:</b> ca. 8+/- 2%<br><b>ROHPLATTE GESCHLIFFEN:</b> Korn 80 oder 100<br><b>ABBILDUNG:</b> Platte geölt</p>
  </article>
  <article class="card card--tall" style="left:204.8px;top:100px">
    <span class="swatch" role="img" aria-label="Holzmuster europäischer Ahorn"></span>
    <h2>Massivholzplatte einschichtig europäischer Ahorn, Möbelbauplatte</h2>
    <p class="subtitle">(Érable européen, lamelles continues)</p>
    <p class="spec"><b>VERFÜGBARE PLATTENSTÄRKEN:</b><br>19, 26, 40, 45 mm<br><b>QUALITÄT:</b> Meisterqualität durchgehende Lamellen (blockverleimt) mit fallender Breite ca. 40 - 80 mm<br><b>SORTIERUNG:</b> A/B<br><b>OBERSEITE:</b> keine Äste, ohne Kern, einheitliche Farbe u. Struktur<br><b>UNTERSEITE:</b> keine Äste, etwas Kern, natürliche Farbdifferenzen erlaubt<br><b>BOT. BEZ.:</b> Acer pseudoplatanus L. wasserfest formaldehydfrei verleimt (D3 nach DIN/EN 204) nur für den Innenbereich<br><b>HOLZFEUCHTE:</b> ca. 8+/- 2%<br><b>ROHPLATTE GESCHLIFFEN:</b> Korn 80 oder 100<br><b>ABBILDUNG:</b> Platte geölt</p>
  </article>
  <article class="card card--tall" style="left:309px;top:100px">
    <span class="swatch" role="img" aria-label="Holzmuster europäischer Ahorn"></span>
    <h2>Massivholzplatte einschichtig europäischer Ahorn, Möbelbauplatte</h2>
    <p class="subtitle">(Érable européen, lamelles continues)</p>
    <p class="spec"><b>VERFÜGBARE PLATTENSTÄRKEN:</b><br>19, 26, 40, 45 mm<br><b>QUALITÄT:</b> Meisterqualität durchgehende Lamellen (blockverleimt) mit fallender Breite ca. 40 - 80 mm<br><b>SORTIERUNG:</b> A/B<br><b>OBERSEITE:</b> keine Äste, ohne Kern, einheitliche Farbe u. Struktur<br><b>UNTERSEITE:</b> keine Äste, etwas Kern, natürliche Farbdifferenzen erlaubt<br><b>BOT. BEZ.:</b> Acer pseudoplatanus L. wasserfest formaldehydfrei verleimt (D3 nach DIN/EN 204) nur für den Innenbereich<br><b>HOLZFEUCHTE:</b> ca. 8+/- 2%<br><b>ROHPLATTE GESCHLIFFEN:</b> Korn 80 oder 100<br><b>ABBILDUNG:</b> Platte geölt</p>
  </article>
  <article class="card card--tall" style="left:93.5px;top:390px">
    <span class="swatch" role="img" aria-label="Holzmuster europäischer Ahorn"></span>
    <h2>Massivholzplatte einschichtig europäischer Ahorn, Möbelbauplatte</h2>
    <p class="subtitle">(Érable européen, lamelles continues)</p>
    <p class="spec"><b>VERFÜGBARE PLATTENSTÄRKEN:</b><br>19, 26, 40, 45 mm<br><b>QUALITÄT:</b> Meisterqualität durchgehende Lamellen (blockverleimt) mit fallender Breite ca. 40 - 80 mm<br><b>SORTIERUNG:</b> A/B<br><b>OBERSEITE:</b> keine Äste, ohne Kern, einheitliche Farbe u. Struktur<br><b>UNTERSEITE:</b> keine Äste, etwas Kern, natürliche Farbdifferenzen erlaubt<br><b>BOT. BEZ.:</b> Acer pseudoplatanus L. wasserfest formaldehydfrei verleimt (D3 nach DIN/EN 204) nur für den Innenbereich<br><b>HOLZFEUCHTE:</b> ca. 8+/- 2%<br><b>ROHPLATTE GESCHLIFFEN:</b> Korn 80 oder 100<br><b>ABBILDUNG:</b> Platte geölt</p>
  </article>
  <article class="card card--tall" style="left:204.8px;top:390px">
    <span class="swatch" role="img" aria-label="Holzmuster europäischer Ahorn"></span>
    <h2>Massivholzplatte einschichtig europäischer Ahorn, Möbelbauplatte</h2>
    <p class="subtitle">(Érable européen, lamelles continues)</p>
    <p class="spec"><b>VERFÜGBARE PLATTENSTÄRKEN:</b><br>19, 26, 40, 45 mm<br><b>QUALITÄT:</b> Meisterqualität durchgehende Lamellen (blockverleimt) mit fallender Breite ca. 40 - 80 mm<br><b>SORTIERUNG:</b> A/B<br><b>OBERSEITE:</b> keine Äste, ohne Kern, einheitliche Farbe u. Struktur<br><b>UNTERSEITE:</b> keine Äste, etwas Kern, natürliche Farbdifferenzen erlaubt<br><b>BOT. BEZ.:</b> Acer pseudoplatanus L. wasserfest formaldehydfrei verleimt (D3 nach DIN/EN 204) nur für den Innenbereich<br><b>HOLZFEUCHTE:</b> ca. 8+/- 2%<br><b>ROHPLATTE GESCHLIFFEN:</b> Korn 80 oder 100<br><b>ABBILDUNG:</b> Platte geölt</p>
  </article>
  <article class="card card--tall" style="left:309px;top:390px">
    <span class="swatch" role="img" aria-label="Holzmuster europäischer Ahorn"></span>
    <h2>Massivholzplatte einschichtig europäischer Ahorn, Möbelbauplatte</h2>
    <p class="subtitle">(Érable européen, lamelles continues)</p>
    <p class="spec"><b>VERFÜGBARE PLATTENSTÄRKEN:</b><br>19, 26, 40, 45 mm<br><b>QUALITÄT:</b> Meisterqualität durchgehende Lamellen (blockverleimt) mit fallender Breite ca. 40 - 80 mm<br><b>SORTIERUNG:</b> A/B<br><b>OBERSEITE:</b> keine Äste, ohne Kern, einheitliche Farbe u. Struktur<br><b>UNTERSEITE:</b> keine Äste, etwas Kern, natürliche Farbdifferenzen erlaubt<br><b>BOT. BEZ.:</b> Acer pseudoplatanus L. wasserfest formaldehydfrei verleimt (D3 nach DIN/EN 204) nur für den Innenbereich<br><b>HOLZFEUCHTE:</b> ca. 8+/- 2%<br><b>ROHPLATTE GESCHLIFFEN:</b> Korn 80 oder 100<br><b>ABBILDUNG:</b> Platte geölt</p>
  </article>

  <!-- right page -->
  <div class="divider" style="left:665px;top:52px;height:614px"></div>
  <div class="divider" style="left:801px;top:52px;height:614px"></div>
  <h1 class="page-title page-title--vertical">HOLZARTEN</h1>

  <article class="card card--wide" style="left:536px;top:52px">
    <span class="swatch" role="img" aria-label="Holzmuster europäischer Ahorn"></span>
    <h2>Massivholzplatte einschichtig europäischer Ahorn, Möbelbauplatte</h2>
    <p class="subtitle">(Érable européen, lamelles continues)</p>
    <div class="spec-grid">
      <p class="spec"><b>VERFÜGBARE PLATTEN-STÄRKEN:</b><br>19, 26, 40, 45 mm<br><b>QUALITÄT:</b> Meisterqualität durchgehende Lamellen (blockverleimt) mit fallender Breite ca. 40 - 80 mm<br><b>SORTIERUNG:</b> A/B<br><b>OBERSEITE:</b> keine Äste, ohne Kern, einheitliche Farbe u. Struktur<br><b>UNTERSEITE:</b> keine Äste, etwas Kern, natürliche Farbdifferenzen erlaubt</p>
      <p class="spec"><b>BOT. BEZ.:</b> Acer pseudoplatanus L. wasserfest formaldehydfrei verleimt (D3 nach DIN/EN 204) nur für den Innenbereich<br><b>HOLZFEUCHTE:</b> ca. 8+/- 2%<br><b>ROHPLATTE GESCHLIFF-EN:</b> Korn 80 oder 100<br><b>ABBILDUNG:</b> Platte geölt</p>
    </div>
  </article>
  <article class="card card--wide" style="left:672.6px;top:52px">
    <span class="swatch" role="img" aria-label="Holzmuster europäischer Ahorn"></span>
    <h2>Massivholzplatte einschichtig europäischer Ahorn, Möbelbauplatte</h2>
    <p class="subtitle">(Érable européen, lamelles continues)</p>
    <div class="spec-grid">
      <p class="spec"><b>VERFÜGBARE PLATTEN-STÄRKEN:</b><br>19, 26, 40, 45 mm<br><b>QUALITÄT:</b> Meisterqualität durchgehende Lamellen (blockverleimt) mit fallender Breite ca. 40 - 80 mm<br><b>SORTIERUNG:</b> A/B<br><b>OBERSEITE:</b> keine Äste, ohne Kern, einheitliche Farbe u. Struktur<br><b>UNTERSEITE:</b> keine Äste, etwas Kern, natürliche Farbdifferenzen erlaubt</p>
      <p class="spec"><b>BOT. BEZ.:</b> Acer pseudoplatanus L. wasserfest formaldehydfrei verleimt (D3 nach DIN/EN 204) nur für den Innenbereich<br><b>HOLZFEUCHTE:</b> ca. 8+/- 2%<br><b>ROHPLATTE GESCHLIFF-EN:</b> Korn 80 oder 100<br><b>ABBILDUNG:</b> Platte geölt</p>
    </div>
  </article>
  <article class="card card--wide" style="left:809px;top:52px">
    <span class="swatch" role="img" aria-label="Holzmuster europäischer Ahorn"></span>
    <h2>Massivholzplatte einschichtig europäischer Ahorn, Möbelbauplatte</h2>
    <p class="subtitle">(Érable européen, lamelles continues)</p>
    <div class="spec-grid">
      <p class="spec"><b>VERFÜGBARE PLATTEN-STÄRKEN:</b><br>19, 26, 40, 45 mm<br><b>QUALITÄT:</b> Meisterqualität durchgehende Lamellen (blockverleimt) mit fallender Breite ca. 40 - 80 mm<br><b>SORTIERUNG:</b> A/B<br><b>OBERSEITE:</b> keine Äste, ohne Kern, einheitliche Farbe u. Struktur<br><b>UNTERSEITE:</b> keine Äste, etwas Kern, natürliche Farbdifferenzen erlaubt</p>
      <p class="spec"><b>BOT. BEZ.:</b> Acer pseudoplatanus L. wasserfest formaldehydfrei verleimt (D3 nach DIN/EN 204) nur für den Innenbereich<br><b>HOLZFEUCHTE:</b> ca. 8+/- 2%<br><b>ROHPLATTE GESCHLIFF-EN:</b> Korn 80 oder 100<br><b>ABBILDUNG:</b> Platte geölt</p>
    </div>
  </article>

  <article class="card card--wide" style="left:536px;top:257.7px">
    <span class="swatch" role="img" aria-label="Holzmuster europäischer Ahorn"></span>
    <h2>Massivholzplatte einschichtig europäischer Ahorn, Möbelbauplatte</h2>
    <p class="subtitle">(Érable européen, lamelles continues)</p>
    <div class="spec-grid">
      <p class="spec"><b>VERFÜGBARE PLATTEN-STÄRKEN:</b><br>19, 26, 40, 45 mm<br><b>QUALITÄT:</b> Meisterqualität durchgehende Lamellen (blockverleimt) mit fallender Breite ca. 40 - 80 mm<br><b>SORTIERUNG:</b> A/B<br><b>OBERSEITE:</b> keine Äste, ohne Kern, einheitliche Farbe u. Struktur<br><b>UNTERSEITE:</b> keine Äste, etwas Kern, natürliche Farbdifferenzen erlaubt</p>
      <p class="spec"><b>BOT. BEZ.:</b> Acer pseudoplatanus L. wasserfest formaldehydfrei verleimt (D3 nach DIN/EN 204) nur für den Innenbereich<br><b>HOLZFEUCHTE:</b> ca. 8+/- 2%<br><b>ROHPLATTE GESCHLIFF-EN:</b> Korn 80 oder 100<br><b>ABBILDUNG:</b> Platte geölt</p>
    </div>
  </article>
  <article class="card card--wide" style="left:672.6px;top:257.7px">
    <span class="swatch" role="img" aria-label="Holzmuster europäischer Ahorn"></span>
    <h2>Massivholzplatte einschichtig europäischer Ahorn, Möbelbauplatte</h2>
    <p class="subtitle">(Érable européen, lamelles continues)</p>
    <div class="spec-grid">
      <p class="spec"><b>VERFÜGBARE PLATTEN-STÄRKEN:</b><br>19, 26, 40, 45 mm<br><b>QUALITÄT:</b> Meisterqualität durchgehende Lamellen (blockverleimt) mit fallender Breite ca. 40 - 80 mm<br><b>SORTIERUNG:</b> A/B<br><b>OBERSEITE:</b> keine Äste, ohne Kern, einheitliche Farbe u. Struktur<br><b>UNTERSEITE:</b> keine Äste, etwas Kern, natürliche Farbdifferenzen erlaubt</p>
      <p class="spec"><b>BOT. BEZ.:</b> Acer pseudoplatanus L. wasserfest formaldehydfrei verleimt (D3 nach DIN/EN 204) nur für den Innenbereich<br><b>HOLZFEUCHTE:</b> ca. 8+/- 2%<br><b>ROHPLATTE GESCHLIFF-EN:</b> Korn 80 oder 100<br><b>ABBILDUNG:</b> Platte geölt</p>
    </div>
  </article>
  <article class="card card--wide" style="left:809px;top:257.7px">
    <span class="swatch" role="img" aria-label="Holzmuster europäischer Ahorn"></span>
    <h2>Massivholzplatte einschichtig europäischer Ahorn, Möbelbauplatte</h2>
    <p class="subtitle">(Érable européen, lamelles continues)</p>
    <div class="spec-grid">
      <p class="spec"><b>VERFÜGBARE PLATTEN-STÄRKEN:</b><br>19, 26, 40, 45 mm<br><b>QUALITÄT:</b> Meisterqualität durchgehende Lamellen (blockverleimt) mit fallender Breite ca. 40 - 80 mm<br><b>SORTIERUNG:</b> A/B<br><b>OBERSEITE:</b> keine Äste, ohne Kern, einheitliche Farbe u. Struktur<br><b>UNTERSEITE:</b> keine Äste, etwas Kern, natürliche Farbdifferenzen erlaubt</p>
      <p class="spec"><b>BOT. BEZ.:</b> Acer pseudoplatanus L. wasserfest formaldehydfrei verleimt (D3 nach DIN/EN 204) nur für den Innenbereich<br><b>HOLZFEUCHTE:</b> ca. 8+/- 2%<br><b>ROHPLATTE GESCHLIFF-EN:</b> Korn 80 oder 100<br><b>ABBILDUNG:</b> Platte geölt</p>
    </div>
  </article>

  <article class="card card--wide" style="left:536px;top:467.5px">
    <span class="swatch" role="img" aria-label="Holzmuster europäischer Ahorn"></span>
    <h2>Massivholzplatte einschichtig europäischer Ahorn, Möbelbauplatte</h2>
    <p class="subtitle">(Érable européen, lamelles continues)</p>
    <div class="spec-grid">
      <p class="spec"><b>VERFÜGBARE PLATTEN-STÄRKEN:</b><br>19, 26, 40, 45 mm<br><b>QUALITÄT:</b> Meisterqualität durchgehende Lamellen (blockverleimt) mit fallender Breite ca. 40 - 80 mm<br><b>SORTIERUNG:</b> A/B<br><b>OBERSEITE:</b> keine Äste, ohne Kern, einheitliche Farbe u. Struktur<br><b>UNTERSEITE:</b> keine Äste, etwas Kern, natürliche Farbdifferenzen erlaubt</p>
      <p class="spec"><b>BOT. BEZ.:</b> Acer pseudoplatanus L. wasserfest formaldehydfrei verleimt (D3 nach DIN/EN 204) nur für den Innenbereich<br><b>HOLZFEUCHTE:</b> ca. 8+/- 2%<br><b>ROHPLATTE GESCHLIFF-EN:</b> Korn 80 oder 100<br><b>ABBILDUNG:</b> Platte geölt</p>
    </div>
  </article>
  <article class="card card--wide" style="left:672.6px;top:467.5px">
    <span class="swatch" role="img" aria-label="Holzmuster europäischer Ahorn"></span>
    <h2>Massivholzplatte einschichtig europäischer Ahorn, Möbelbauplatte</h2>
    <p class="subtitle">(Érable européen, lamelles continues)</p>
    <div class="spec-grid">
      <p class="spec"><b>VERFÜGBARE PLATTEN-STÄRKEN:</b><br>19, 26, 40, 45 mm<br><b>QUALITÄT:</b> Meisterqualität durchgehende Lamellen (blockverleimt) mit fallender Breite ca. 40 - 80 mm<br><b>SORTIERUNG:</b> A/B<br><b>OBERSEITE:</b> keine Äste, ohne Kern, einheitliche Farbe u. Struktur<br><b>UNTERSEITE:</b> keine Äste, etwas Kern, natürliche Farbdifferenzen erlaubt</p>
      <p class="spec"><b>BOT. BEZ.:</b> Acer pseudoplatanus L. wasserfest formaldehydfrei verleimt (D3 nach DIN/EN 204) nur für den Innenbereich<br><b>HOLZFEUCHTE:</b> ca. 8+/- 2%<br><b>ROHPLATTE GESCHLIFF-EN:</b> Korn 80 oder 100<br><b>ABBILDUNG:</b> Platte geölt</p>
    </div>
  </article>
  <article class="card card--wide" style="left:809px;top:467.5px">
    <span class="swatch" role="img" aria-label="Holzmuster europäischer Ahorn"></span>
    <h2>Massivholzplatte einschichtig europäischer Ahorn, Möbelbauplatte</h2>
    <p class="subtitle">(Érable européen, lamelles continues)</p>
    <div class="spec-grid">
      <p class="spec"><b>VERFÜGBARE PLATTEN-STÄRKEN:</b><br>19, 26, 40, 45 mm<br><b>QUALITÄT:</b> Meisterqualität durchgehende Lamellen (blockverleimt) mit fallender Breite ca. 40 - 80 mm<br><b>SORTIERUNG:</b> A/B<br><b>OBERSEITE:</b> keine Äste, ohne Kern, einheitliche Farbe u. Struktur<br><b>UNTERSEITE:</b> keine Äste, etwas Kern, natürliche Farbdifferenzen erlaubt</p>
      <p class="spec"><b>BOT. BEZ.:</b> Acer pseudoplatanus L. wasserfest formaldehydfrei verleimt (D3 nach DIN/EN 204) nur für den Innenbereich<br><b>HOLZFEUCHTE:</b> ca. 8+/- 2%<br><b>ROHPLATTE GESCHLIFF-EN:</b> Korn 80 oder 100<br><b>ABBILDUNG:</b> Platte geölt</p>
    </div>
  </article>
</div>
</body>
</html>
```